Business Card Design

we are a brand new cable TV network devoted to self improvement and leading a better life called FLOURIVO TV.I have a logo. We have 3 executives that need cards.I want it to be a heavy stock card: professional but showing our creative nature

Industry/Entity Type

Business

Contact Information for Business Card

CLAUDIA SAENZ AMLIECEO350 San Juan DrPonte Vedra Beach FL 32082904-473-5953

```html
<!DOCTYPE html>
<html lang="en">
<head>
<meta charset="utf-8">
<title>FLOURIVO TV — Business Card</title>
<link rel="stylesheet" href="https://fonts.googleapis.com/css2?family=Cormorant+Garamond:ital,wght@0,500;1,500&display=swap">
<style>
  :root {
    --backdrop: #e4ddd5;
    --card-white: #ffffff;
    --top-band: #1f1f1f;
    --brand-red: #e0402c;
    --red-light: #e85340;
    --red-dark: #cf3726;
    --band-grey: #3c3c3c;
    --band-grey-light: #474747;
    --band-grey-dark: #333333;
    --logo-ink: #3a3a3a;
    --text-light: #f3f3f3;
  }
  * { box-sizing: border-box; margin: 0; padding: 0; }
  html, body {
    width: 1200px;
    height: 1200px;
    overflow: hidden;
    background: var(--backdrop);
  }
  .card {
    position: absolute;
    left: 100px;
    top: 284px;
    width: 1000px;
    height: 632px;
    background: var(--card-white);
    overflow: hidden;
    box-shadow: 0 30px 50px rgba(0,0,0,0.18);
    font-family: "Cormorant Garamond", Georgia, serif;
  }
  .card__top-band {
    position: absolute;
    left: 0; top: 0;
    width: 100%;
    height: 30px;
    background: var(--top-band);
  }
  .brand {
    position: absolute;
    right: 60px;
    top: 78px;
    display: flex;
    align-items: center;
    gap: 18px;
  }
  .brand__square {
    width: 44px;
    height: 44px;
    background: var(--brand-red);
  }
  .brand__name {
    font-family: "Cormorant Garamond", Georgia, serif;
    font-style: normal;
    font-weight: 500;
    font-size: 70px;
    letter-spacing: 1px;
    color: var(--logo-ink);
    line-height: 1;
  }
  .tiles {
    position: absolute;
    left: 0;
    display: block;
  }
  .tiles--red { top: 292px; width: 538px; height: 138px; }
  .tiles--grey { top: 430px; width: 1000px; height: 202px; }
  .person {
    position: absolute;
    left: 38px;
    top: 304px;
    color: var(--text-light);
    font-style: italic;
    font-weight: 500;
  }
  .person__name {
    font-size: 31px;
    letter-spacing: 1px;
    line-height: 1.1;
  }
  .person__title {
    font-size: 24px;
    line-height: 1.2;
  }
  .contact {
    position: absolute;
    color: var(--text-light);
    font-style: italic;
    font-weight: 500;
    font-size: 30px;
    line-height: 1.35;
  }
  .contact--phone { left: 38px; top: 440px; }
  .contact--address { right: 44px; top: 432px; text-align: right; }
</style>
</head>
<body>
  <div class="card">
    <div class="card__top-band"></div>

    <div class="brand">
      <span class="brand__square"></span>
      <span class="brand__name">FLOURIVO TV</span>
    </div>

    <svg class="tiles tiles--red" viewBox="0 0 538 138" aria-hidden="true">
      <rect width="538" height="138" fill="var(--brand-red)"/>
      <rect x="0" y="0" width="90" height="69" fill="var(--red-dark)"/>
      <rect x="90" y="0" width="90" height="69" fill="var(--brand-red)"/>
      <rect x="180" y="0" width="90" height="69" fill="var(--red-light)"/>
      <rect x="270" y="0" width="90" height="69" fill="var(--red-dark)"/>
      <rect x="360" y="0" width="90" height="69" fill="var(--brand-red)"/>
      <rect x="450" y="0" width="88" height="69" fill="var(--red-light)"/>
      <rect x="0" y="69" width="90" height="69" fill="var(--brand-red)"/>
      <rect x="90" y="69" width="90" height="69" fill="var(--red-dark)"/>
      <rect x="180" y="69" width="90" height="69" fill="var(--brand-red)"/>
      <rect x="270" y="69" width="90" height="69" fill="var(--red-light)"/>
      <rect x="360" y="69" width="90" height="69" fill="var(--red-dark)"/>
      <rect x="450" y="69" width="88" height="69" fill="var(--brand-red)"/>
    </svg>

    <svg class="tiles tiles--grey" viewBox="0 0 1000 202" aria-hidden="true">
      <rect width="1000" height="202" fill="var(--band-grey)"/>
      <rect x="0" y="0" width="160" height="80" fill="var(--band-grey-light)"/>
      <rect x="160" y="0" width="150" height="80" fill="var(--band-grey)"/>
      <rect x="310" y="0" width="180" height="80" fill="var(--band-grey-dark)"/>
      <rect x="490" y="0" width="170" height="80" fill="var(--band-grey-light)"/>
      <rect x="660" y="0" width="170" height="80" fill="var(--band-grey)"/>
      <rect x="830" y="0" width="170" height="80" fill="var(--band-grey-dark)"/>
      <rect x="0" y="80" width="200" height="122" fill="var(--band-grey-dark)"/>
      <rect x="200" y="80" width="180" height="122" fill="var(--band-grey-light)"/>
      <rect x="380" y="80" width="200" height="122" fill="var(--band-grey)"/>
      <rect x="580" y="80" width="210" height="122" fill="var(--band-grey-dark)"/>
      <rect x="790" y="80" width="210" height="122" fill="var(--band-grey-light)"/>
    </svg>

    <div class="person">
      <p class="person__name">MIRELLA OKAFOR DUNST</p>
      <p class="person__title">CEO</p>
    </div>

    <p class="contact contact--phone">904-618-2047</p>
    <p class="contact contact--address">718 Harlow Creek Dr<br>Ponte Vedra Beach FL 32097</p>
  </div>
</body>
</html>
```